Stationery Design Project

We need a stationery design for our Norwegian trucking company. We have existed for about 15 years and our 12 drivers uses relatively new vehicles to transport goods around in northern Norway. Long distance routes with fresh fish og food transport is our main operations.

We have already made alogo that's printed on our trucks. The logo and a picture of our trucks is attached. I think the logo i crappy, but since its already in use, changing it is not an option in this round. Still using a better colour scheme in the overall stationery and more interesting fonts is possible (altso in the logo).

Company details:
Name: Vikmarka AS
Organisation nr 983 517 608
Post adress: 8640 Brekka

I like minimalism and simplicity. I am avalibly for questions in normal GMT working hours either here or on mail: kjell@brekkafrakt.no

Reason: Hi. Im extending the deadline because I needed some time to find a vector file of our logo. Sorry for the inconvenience

Hi, and thanks for all your interest in the project. Some updates:

-          I have decided to commit to using one of the designs. Some designer will get the payment.

-          I have extended the deadline with 24 hours since I needed some time to find our firms vector logo (a slow Swedish man was holding me up)

-          We will not choose a design before the deadline. No need to rush.

-          We have received a lot of great design and think there is a need to specified the product we want to make:

o   Business Card for all our employers. I just need the design and will duplicate with the correct numbers and name myself. The information on should be: Logo, employer’s name, Phone number, email, website, Postal number and address. Use this as a template: logo, Leif Dahlberg, 47382950, Leif@brekkafrakt.no,, brekkafrakt.no, 8640 Brekka. The order and placement of the information is your creative decision.

o   Stickers to put on the goods we travel. On the sticker the should be the following information: Logo, phone number, Tekst and link: Fraktæ av Vikmarka. Ke du syns? Brekkafrakt.no/tilbakemelding (this means: Handled by Vikmarka. What do you think Brekkafrakt.no/feedback -à the link will be a feedback form). The placement the information and size is your creative decision with some stings: we have been thinking of using Prentolo for printing and see that a size about 6x6 cm, 8x5 or something like that. (with 3000 copies our budget is 200 punds). Any suggestions of other suppliers are welcome. Prentolo price calculator http://www.prentoloprints.example/digital-litho-printing/printing-labels-tags/stickers/

o   Letterhead with logo, address, phone number and organizational number.

o   Envelopes with logo,address, phone number and organizational number.

Have a nice day.

 

 

• Using the blue colour in the logo and using a similar graphic approch.

```html
<!DOCTYPE html>
<html lang="no">
<head>
<meta charset="utf-8">
<title>Vikmarka – visittkort</title>
<link rel="stylesheet" href="https://fonts.googleapis.com/css2?family=Source+Sans+3:wght@400;600;700&display=swap">
<style>
  :root {
    --backdrop: #9a9a9a;
    --paper: #ffffff;
    --blue-deep: #0b4fa3;
    --blue-bright: #0a75c0;
    --ink: #222222;
    --rule: #b5b5b5;
  }
  * { box-sizing: border-box; margin: 0; padding: 0; }
  html, body { width: 1200px; height: 711px; overflow: hidden; }
  body {
    position: relative;
    background: var(--backdrop);
    font-family: "Source Sans 3", "Myriad Pro", Arial, sans-serif;
  }
  .card {
    position: absolute;
    width: 514px;
    height: 294px;
    background: var(--paper);
    box-shadow: 0 0 0 1px rgba(0,0,0,0.18);
    overflow: hidden;
  }
  .card--front { left: 66px; top: 45px; }
  .card--back-deep { left: 620px; top: 45px; background: var(--blue-deep); }
  .card--back-white { left: 66px; top: 370px; }
  .card--back-bright { left: 620px; top: 370px; background: var(--blue-bright); }

  .brand {
    position: absolute;
    left: 0; right: 0;
    display: flex;
    align-items: center;
    justify-content: center;
    gap: 14px;
    font-weight: 700;
    font-size: 56px;
    letter-spacing: 0.5px;
    color: var(--blue-deep);
  }
  .brand__dot {
    width: 22px; height: 22px;
    border-radius: 50%;
    background: currentColor;
  }
  .card--front .brand { top: 42px; }
  .card--back-white .brand,
  .card--back-deep .brand,
  .card--back-bright .brand { top: 100px; }
  .card--back-deep .brand,
  .card--back-bright .brand { color: var(--paper); }

  .website {
    position: absolute;
    left: 0; right: 0;
    top: 243px;
    text-align: center;
    font-size: 18px;
    letter-spacing: 3.6px;
    color: var(--ink);
  }
  .card--back-deep .website,
  .card--back-bright .website { color: var(--paper); }

  .name-band {
    position: absolute;
    left: 0; right: 0;
    top: 164px;
    height: 39px;
    border-top: 2px solid var(--blue-bright);
    border-bottom: 2px solid var(--blue-bright);
  }
  .name-band__bar {
    position: absolute;
    left: 0; right: 0;
    top: 4px; bottom: 4px;
    background: var(--blue-deep);
    color: var(--paper);
    font-weight: 700;
    font-size: 18px;
    display: flex;
    align-items: center;
    justify-content: center;
  }

  .holder {
    position: absolute;
    right: 268px;
    top: 224px;
    text-align: right;
  }
  .holder__name {
    font-weight: 700;
    font-size: 20px;
    color: var(--blue-deep);
    line-height: 24px;
  }
  .holder__org {
    font-size: 15.5px;
    color: var(--blue-bright);
    line-height: 20px;
  }
  .divider {
    position: absolute;
    left: 256px;
    top: 212px;
    width: 1px;
    height: 67px;
    background: var(--rule);
  }
  .contact {
    position: absolute;
    left: 268px;
    top: 220px;
    list-style: none;
    font-size: 15.5px;
    color: var(--ink);
    line-height: 20px;
  }
  .contact li { display: flex; align-items: center; gap: 4px; }
  .contact svg { width: 12px; height: 12px; fill: var(--blue-deep); }
</style>
</head>
<body>

  <section class="card card--front" aria-label="Visittkort forside">
    <div class="brand"><span class="brand__dot"></span>Vikmarka</div>
    <div class="name-band"><div class="name-band__bar">Leif Dahlberg</div></div>
    <div class="holder">
      <p class="holder__name">Leif Dahlberg</p>
      <p class="holder__org">Org nr 983 517 608</p>
    </div>
    <div class="divider"></div>
    <ul class="contact">
      <li>
        <svg viewBox="0 0 12 12" aria-hidden="true"><path d="M6 1 L11 5 L10 5 L10 11 L2 11 L2 5 L1 5 Z"/></svg>
        8640 Brekka
      </li>
      <li>
        <svg viewBox="0 0 12 12" aria-hidden="true"><path d="M3 1 L5 1 L5.5 4 L4 5 C4.6 6.6 5.4 7.4 7 8 L8 6.5 L11 7 L11 9 C11 10 10 11 9 11 C4.5 10.5 1.5 7.5 1 3 C1 2 2 1 3 1 Z"/></svg>
        47382950
      </li>
      <li>
        <svg viewBox="0 0 12 12" aria-hidden="true"><path d="M1 3 L11 3 L11 10 L1 10 Z M1.8 3.6 L6 7 L10.2 3.6 Z" fill-rule="evenodd"/></svg>
        Leif@brekkafrakt.no
      </li>
    </ul>
  </section>

  <section class="card card--back-deep" aria-label="Visittkort bakside mørkeblå">
    <div class="brand"><span class="brand__dot"></span>Vikmarka</div>
    <p class="website">www.brekkafrakt.no</p>
  </section>

  <section class="card card--back-white" aria-label="Visittkort bakside hvit">
    <div class="brand"><span class="brand__dot"></span>Vikmarka</div>
    <p class="website">www.brekkafrakt.no</p>
  </section>

  <section class="card card--back-bright" aria-label="Visittkort bakside lyseblå">
    <div class="brand"><span class="brand__dot"></span>Vikmarka</div>
    <p class="website">www.brekkafrakt.no</p>
  </section>

</body>
</html>
```